New Law Firm Corporate Identity Project

Newly started law firm needs a corporate identity. The theme behind the corporate identity should be simple and elegant, yet professional.
What I need as part of this corporate identity kit (CIK) is a designed logo, letterhead, and business card.
Also, I would like to have an easily transferable electronic version of whatever you design, so that I can copy and paste this logo, etc. on Microsoft Word, for example. I would like the delivery of the logo, business card, and letterhead in high-res PSD and AI formats in CS1 and CS3, which can be resized later to any resolution possible (print ready included). I will then own the rights to the content once the work has been paid for. Since I will need multiple formats - .psd (CS1 and CS3), .ai (CS1 and CS3), .jpg, and .gif.
The name of the law firm is "Law Offices of Merrick Sollberg, APC". I would like my initials, "M" and "S" incorporated into the logo
The logo and CIK that I prefer would not look like the traditional law firm logo, with a guy being arrested, or of a building, or of the blindfolded lady balancing a scale. I prefer something modern and trendy, yet without the logo or CIK being too bland, too much, or looking “overcrowded”.
I'm not too particular on the color combinations, but I would like my logo and letterhead to stand out and look smart in terms of color combinations and design. Furthermore, I would like my logo to still be clearly seen after it has been photocopied.
Please use your creativity and create something original, such as hand-drawn art, as opposed to using clip-art.
Thanks in advance!
Reason: I changed the status of the project to guaranteed payment, and therefore, would like to see more logo options before deciding on which one to select. Thanks, and please keep submitting your proposals.
Electronic
Law Offices of Merrick Sollberg, APC. Incorporated into the actual logo are the letters "M" and "S".

```html
<!DOCTYPE html>
<html lang="en">
<head>
<meta charset="utf-8">
<title>Law Offices of Merrick Sollberg, APC – Stationery</title>
<link href="https://fonts.googleapis.com/css2?family=Tenor+Sans&display=swap" rel="stylesheet">
<style>
  :root {
    --brand-blue: #06538a;
    --ink-grey: #4a4a4a;
    --paper: #ffffff;
    --backdrop: #e8e6e2;
    --edge: #d4d1cc;
  }
  * { box-sizing: border-box; margin: 0; padding: 0; }
  html, body { width: 1200px; height: 1200px; overflow: hidden; }
  body {
    background: var(--backdrop);
    font-family: "Tenor Sans", "Optima", sans-serif;
    color: var(--ink-grey);
    position: relative;
  }
  .sheet {
    position: absolute;
    background: var(--paper);
    border: 1px solid var(--edge);
  }

  /* Wordmark: plain square + firm name in a single colour and weight */
  .wordmark { position: absolute; display: flex; align-items: flex-end; gap: 8px; color: var(--brand-blue); }
  .wordmark__square { background: var(--brand-blue); flex: none; }
  .wordmark__text { line-height: 1.05; text-transform: uppercase; }
  .wordmark__small { display: block; }
  .wordmark__large { display: block; }

  .address { position: absolute; line-height: 1.2; text-align: right; }

  /* Letterhead */
  .letterhead { left: 97px; top: 66px; width: 758px; height: 1072px; }
  .letterhead .wordmark { left: 33px; top: 52px; }
  .letterhead .wordmark__square { width: 34px; height: 34px; }
  .letterhead .wordmark__small { font-size: 11.5px; }
  .letterhead .wordmark__large { font-size: 19.5px; }
  .letterhead .address { right: 25px; top: 52px; font-size: 11.5px; }
  .letterhead__tab { position: absolute; right: -1px; top: 44px; width: 18px; height: 46px; background: var(--brand-blue); }

  /* Business card */
  .card { left: 791px; top: 326px; width: 372px; height: 226px; }
  .card .wordmark { left: 14px; top: 14px; gap: 5px; }
  .card .wordmark__square { width: 22px; height: 22px; }
  .card .wordmark__small { font-size: 7px; }
  .card .wordmark__large { font-size: 12.5px; }
  .card .address { left: 14px; top: 46px; font-size: 7.5px; text-align: left; line-height: 1.1; }
  .card__holder { position: absolute; left: 190px; top: 130px; }
  .card__name { color: var(--brand-blue); font-size: 11.5px; text-transform: uppercase; }
  .card__role { font-size: 10px; }
  .card__contacts { position: absolute; left: 190px; top: 164px; font-size: 8.5px; line-height: 1.18; border-collapse: collapse; }
  .card__contacts th { color: var(--brand-blue); font-weight: normal; text-align: left; padding-right: 14px; }

  /* Envelope */
  .envelope { left: 316px; top: 576px; width: 847px; height: 482px; border: none; background: transparent; }
  .envelope__flap { position: absolute; left: 0; top: 0; width: 847px; height: 58px; }
  .envelope__face { position: absolute; left: 0; top: 57px; width: 847px; height: 425px; background: var(--paper); border: 1px solid var(--edge); }
  .envelope .wordmark { left: 30px; top: 40px; }
  .envelope .wordmark__square { width: 44px; height: 44px; }
  .envelope .wordmark__small { font-size: 12.5px; }
  .envelope .wordmark__large { font-size: 21px; }
  .envelope .address { left: 30px; width: 278px; top: 98px; font-size: 12.5px; }
  .envelope__web { position: absolute; left: 20px; top: 380px; font-size: 12.5px; color: var(--brand-blue); }
  .envelope__web-bar { position: absolute; left: 0; top: 374px; width: 8px; height: 48px; background: var(--brand-blue); }
</style>
</head>
<body>

<section class="sheet letterhead" aria-label="Letterhead">
  <div class="wordmark">
    <span class="wordmark__square"></span>
    <span class="wordmark__text">
      <span class="wordmark__small">Law Offices of</span>
      <span class="wordmark__large">Merrick Sollberg, APC</span>
    </span>
  </div>
  <address class="address" style="font-style:normal">1480 Harbor View Drive<br>Suite 310<br>Long Beach, 90802</address>
  <span class="letterhead__tab"></span>
</section>

<section class="envelope sheet" aria-label="Envelope">
  <svg class="envelope__flap" viewBox="0 0 847 58" aria-hidden="true">
    <path d="M0 58 C18 28 36 0 56 0 L791 0 C811 0 829 28 847 58 Z" fill="var(--brand-blue)"/>
  </svg>
  <div class="envelope__face">
    <div class="wordmark">
      <span class="wordmark__square"></span>
      <span class="wordmark__text">
        <span class="wordmark__small">Law Offices of</span>
        <span class="wordmark__large">Merrick Sollberg, APC</span>
      </span>
    </div>
    <address class="address" style="font-style:normal">1480 Harbor View Drive<br>Suite 310<br>Long Beach, 90802</address>
    <span class="envelope__web-bar"></span>
    <span class="envelope__web">www.sollberg-law.com</span>
  </div>
</section>

<section class="sheet card" aria-label="Business card">
  <div class="wordmark">
    <span class="wordmark__square"></span>
    <span class="wordmark__text">
      <span class="wordmark__small">Law Offices of</span>
      <span class="wordmark__large">Merrick Sollberg, APC</span>
    </span>
  </div>
  <address class="address" style="font-style:normal">1480 Harbor View Drive<br>Suite 310<br>Long Beach, 90802</address>
  <div class="card__holder">
    <p class="card__name">Merrick Sollberg, APC</p>
    <p class="card__role">Director</p>
  </div>
  <table class="card__contacts">
    <tr><th>P.</th><td>555.014.2207</td></tr>
    <tr><th>F.</th><td>555.014.2208</td></tr>
    <tr><th>E.</th><td>merrick@sollberg-law.com</td></tr>
    <tr><th>w.</th><td>www.sollberg-law.com</td></tr>
  </table>
</section>

</body>
</html>
```